School website design - Technology and the arts

We will need a new or updated design that incorporates the following features:
-Reactive design that changes with the needs of the device.
-Static Background - only content scrolls
-Static Menu - similar to the Wordpress Quiet harbor theme
-Alert box for important notices (closings/emergency use only) that doesn’t display unless active
-Margins must be wider than “standard wordpress theme” (fits the entire display at any resolution, doesn’t just center a columned design)
-Features an image scroll on the front page to show our current works/progress. (only if the screen is big enough). Should have swipe capability
-We must have a place on the front page to display the current school news as well as a location to display current events with a poster (see current webdesign for example)
-Uses the school colors (green and gold/yellow) in a way that is pleasing to the eye.
-Unique design to our school that is very clean and modern.
-Events need to be able to pop-out when you mouseover in a desktop environment. Example: http://plumvaultly.net/category/wordpress/creative (mouse over a theme and it shows additional information about it without a refresh)
-Custom Admin panel to easily updated the news and events section.
-Notes: We are currently using some free icons that we found to make the current site look not so boring since we do not have a lot of content on each page. We would like to step away from that and are open to suggestions. Possibly something like http://dovrami.com/demo/?theme=brook under the services section but smaller.
-Notes 2: We have plenty of pictures of our building and activities that can be used as a background, etc.
-We are open to new ideas and suggestions.

Our current website is https://www.mlvt.us to get an idea on how we manage our current site.

```html
<!DOCTYPE html>
<html lang="en">
<head>
<meta charset="utf-8">
<title>Marlowe Valley Regional Governor's School</title>
<link href="https://fonts.googleapis.com/css2?family=Cabin:wght@400;500;600&family=Playfair+Display:wght@400&display=swap" rel="stylesheet">
<style>
:root{
  --grass:#3f8a2c;
  --grass-dark:#2c6a1d;
  --green:#1f6a12;
  --green-deep:#175009;
  --gold:#f2d437;
  --orange:#f5a623;
  --cream:#ece6d8;
  --text:#4a4a4a;
  --muted:#9a9a9a;
  --red:#a3231b;
  --link:#2d5e2a;
  --panel:#f0f0f0;
  --footer:#3b3e41;
  --footer-deep:#303335;
  --white:#ffffff;
}
*{box-sizing:border-box;margin:0;padding:0}
html,body{width:1200px;height:2757px;overflow:hidden}
body{background:linear-gradient(180deg,var(--grass),var(--grass-dark));font-family:"Cabin",sans-serif;color:var(--text);position:relative}
.page{position:absolute;left:77px;top:0;width:1038px;height:2757px;background:var(--white);box-shadow:0 0 18px rgba(0,0,0,.45);overflow:hidden}
.serif{font-family:"Playfair Display",serif}

/* header */
.site-header{height:165px;background:var(--cream);position:relative}
.brand{position:absolute;left:40px;top:48px;display:flex;align-items:center;gap:14px}
.brand-mark{width:56px;height:56px;border-radius:50%;background:var(--green)}
.brand-name{font-size:22px;font-weight:600;color:var(--green);line-height:1.15;width:200px}
.address{position:absolute;right:16px;top:50px;font-size:13px;color:#222;display:flex;align-items:center;gap:8px;white-space:nowrap}
.quick-links{position:absolute;right:86px;top:103px;display:flex;gap:26px;font-size:12.5px;color:#222}
.quick-links span{display:flex;align-items:center;gap:8px;white-space:nowrap}

/* nav */
.main-nav{height:52px;background:linear-gradient(180deg,#2f8a1c,var(--green-deep));display:flex;padding-left:22px}
.main-nav a{color:var(--white);text-decoration:none;font-size:13.5px;padding:0 16px;line-height:52px;white-space:nowrap}
.main-nav a.active{background:linear-gradient(180deg,#f8d94a,#f1b526)}

/* hero */
.hero{height:408px;position:relative;background:linear-gradient(110deg,#6b4a3a 0%,#a79683 30%,#d9d2c6 55%,#8e8a86 80%,#d8d4cc 100%)}
.hero-title{position:absolute;left:0;top:220px;height:54px;padding:0 90px 0 22px;white-space:nowrap;background:linear-gradient(90deg,rgba(248,224,80,.95),rgba(248,224,80,.6) 80%,rgba(248,224,80,0));font-size:29px;font-weight:400;line-height:54px;color:var(--green)}
.slider-arrows{position:absolute;left:20px;top:343px;display:flex;gap:6px}
.slider-arrows span{width:30px;height:30px;border-radius:50%;border:2px solid rgba(255,255,255,.8);background:rgba(0,0,0,.15);display:flex;align-items:center;justify-content:center}

/* welcome */
.welcome{height:230px;background:linear-gradient(180deg,#f7e24a,var(--orange));text-align:center;padding-top:18px}
.welcome h2{font-size:23px;font-weight:400;color:#4a3a10;letter-spacing:.5px}
.welcome p{width:1000px;margin:16px auto 0;font-size:14px;line-height:31px;color:#6b5420}
.btn-green{display:inline-block;margin-top:12px;background:linear-gradient(180deg,#2f8a1c,var(--green-deep));color:var(--white);font-size:13.5px;padding:10px 14px;border-radius:4px}

/* section headings */
.section-label{display:inline-block;height:50px;line-height:50px;padding:0 64px 0 18px;font-size:15.5px;font-weight:400;color:#333;background:linear-gradient(90deg,var(--gold),rgba(242,212,55,.5) 70%,rgba(242,212,55,0));border-left:4px solid var(--gold)}

/* news */
.news{height:419px;padding:30px 22px 0;border-bottom:1px solid #ddd}
.news-grid{display:flex;gap:19px;margin-top:34px}
.news-card{width:235px}
.news-photo{height:128px;border:4px solid #e6e6e6;box-shadow:0 8px 8px -6px rgba(0,0,0,.35)}
.news-card h3{font-size:14px;font-weight:400;color:var(--link);margin-top:33px;white-space:nowrap}
.meta{display:flex;align-items:center;gap:8px;color:var(--red);font-size:12.5px;white-space:nowrap}
.meta.date{margin-top:13px}
.meta.place{margin-top:16px;font-size:10.5px}

/* current events */
.events{height:625px;background:var(--panel);padding:44px 22px 0;border-bottom:1px solid #ddd}
.events-grid{display:flex;gap:27px;margin-top:40px}
.event-card{width:318px;height:465px;background:var(--white);box-shadow:0 1px 4px rgba(0,0,0,.15)}
.event-photo{height:193px}
.event-card .meta{font-size:12px;font-weight:600;padding-left:20px}
.event-card .meta.when{margin-top:40px}
.event-card .meta.where{margin-top:18px}
.event-card p{padding:0 22px;margin-top:28px;font-size:13.5px;line-height:25px;text-align:justify;color:#444;height:75px;overflow:hidden}
.btn-ghost{display:block;margin:28px auto 0;width:112px;height:38px;line-height:36px;text-align:center;border:1px solid #ccc;border-radius:19px;font-size:13px;color:#444;background:var(--white)}

/* upcoming */
.upcoming{height:485px;padding:36px 22px 0}
.upcoming-grid{display:flex;justify-content:space-between;margin-top:40px}
.upcoming-item{width:238px;text-align:center}
.ring{width:203px;height:203px;margin:0 auto;border-radius:50%;background:#f3f3f3;padding:10px;box-shadow:0 1px 3px rgba(0,0,0,.15)}
.ring div{width:183px;height:183px;border-radius:50%}
.upcoming-item h3{font-size:17px;font-weight:400;color:#222;margin-top:34px;white-space:nowrap}
.upcoming-item p{width:200px;margin:4px auto 0;font-size:13px;line-height:26px;color:var(--muted)}

/* footer */
.site-footer{height:281px;background:var(--footer);color:#ddd;position:relative}
.footer-col{position:absolute;top:50px}
.footer-col h4{font-size:14.5px;font-weight:400;color:var(--white);margin-bottom:20px;white-space:nowrap}
.contact-line{display:flex;gap:10px;font-size:12px;line-height:20px;margin-bottom:10px;color:#ccc}
.post{font-size:13px;line-height:24px;color:#ddd;width:270px}
.post small{display:block;font-size:11.5px;color:#bbb}
.post + .post{border-top:1px solid #666;margin-top:16px;padding-top:16px}
.mail-field{width:207px;height:40px;background:#555;border:1px solid #666;font-size:12.5px;color:#888;line-height:38px;padding-left:16px}
.btn-sub{width:124px;height:40px;margin-top:20px;background:linear-gradient(180deg,#2f8a1c,var(--green-deep));color:var(--white);font-size:13.5px;line-height:40px;text-align:center}
.social{display:flex;gap:8px}
.social span{width:26px;height:26px;border-radius:50%;background:#eee}
.copyright{height:92px;background:var(--footer-deep);text-align:center;line-height:92px;font-size:12px;color:#888}
</style>
</head>
<body>
<div class="page">

  <header class="site-header">
    <div class="brand">
      <span class="brand-mark"></span>
      <span class="brand-name">Marlowe Valley Falcons</span>
    </div>
    <div class="address">
      <svg width="20" height="18" viewBox="0 0 20 18"><path d="M10 1 1 9h3v8h5v-5h2v5h5V9h3z" fill="#222"/></svg>
      418 East Linden Street, Dalton Ridge, VA 23990, United States
    </div>
    <div class="quick-links">
      <span><svg width="14" height="10" viewBox="0 0 14 10"><rect width="14" height="10" fill="#222"/><path d="M0 0l7 6 7-6" stroke="#ece6d8" fill="none"/></svg>MVRGS Email</span>
      <span><svg width="14" height="13" viewBox="0 0 14 13"><rect x=".5" y="1.5" width="13" height="11" fill="none" stroke="#222"/><rect x=".5" y="1.5" width="13" height="3" fill="#222"/></svg>Calendars</span>
      <span><svg width="9" height="14" viewBox="0 0 9 14"><rect width="9" height="14" rx="1.5" fill="#222"/><rect x="1.5" y="2" width="6" height="8" fill="#ece6d8"/></svg>Contact Us</span>
    </div>
  </header>

  <nav class="main-nav">
    <a class="active">Home</a><a>About MVRGS</a><a>Students/Parents</a><a>Faculty/Staff</a><a>Documents/Forms</a><a>Programs of Study</a><a>Services</a>
  </nav>

  <section class="hero" role="img" aria-label="Photo of a school hallway with a row of lockers">
    <h1 class="hero-title serif">Marlowe Valley Regional Governor's School</h1>
    <div class="slider-arrows">
      <span><svg width="10" height="12" viewBox="0 0 10 12"><path d="M7 1 2 6l5 5" stroke="#fff" stroke-width="2" fill="none"/></svg></span>
      <span><svg width="10" height="12" viewBox="0 0 10 12"><path d="M3 1l5 5-5 5" stroke="#fff" stroke-width="2" fill="none"/></svg></span>
    </div>
  </section>

  <section class="welcome">
    <h2 class="serif">WELCOME TO OUR SCHOOL</h2>
    <p>The Marlowe Valley Regional Governor's School for the Arts and Technology provides gifted and talented students a differentiated and rigorous education, cultivates a supportive environment that inspires unique artistic and technological visions, promotes cultural tolerance, nurtures community partnerships, and produces active, engaged citizens.</p>
    <span class="btn-green">Learn More</span>
  </section>

  <section class="news">
    <h2 class="section-label">Latest News</h2>
    <div class="news-grid">
      <article class="news-card">
        <div class="news-photo" role="img" aria-label="Soccer ball in a goal net" style="background:linear-gradient(135deg,#3a5f9e,#c9cdd6 55%,#2b3f6a)"></div>
        <h3>Varsity Boys' Soccer match...</h3>
        <div class="meta date"><svg width="12" height="12" viewBox="0 0 12 12"><circle cx="6" cy="6" r="5" fill="none" stroke="#888"/><path d="M6 3v3h2" stroke="#888" fill="none"/></svg>Mon, March 31</div>
        <div class="meta place"><svg width="8" height="11" viewBox="0 0 8 11"><path d="M4 0a4 4 0 0 0-4 4c0 3 4 7 4 7s4-4 4-7a4 4 0 0 0-4-4z" fill="#bbb"/></svg>East Linden Street, United States</div>
      </article>
      <article class="news-card">
        <div class="news-photo" role="img" aria-label="Tennis ball beside a racket on blue" style="background:linear-gradient(135deg,#e8eef5,#2f7fe0 45%,#1f63c8)"></div>
        <h3>Home Tennis match...</h3>
        <div class="meta date"><svg width="12" height="12" viewBox="0 0 12 12"><circle cx="6" cy="6" r="5" fill="none" stroke="#888"/><path d="M6 3v3h2" stroke="#888" fill="none"/></svg>Mon, March 31</div>
        <div class="meta place"><svg width="8" height="11" viewBox="0 0 8 11"><path d="M4 0a4 4 0 0 0-4 4c0 3 4 7 4 7s4-4 4-7a4 4 0 0 0-4-4z" fill="#bbb"/></svg>East Linden Street, United States</div>
      </article>
      <article class="news-card">
        <div class="news-photo" role="img" aria-label="Tennis ball at a net on a blue court" style="background:linear-gradient(180deg,#1b2330,#3c4f6b 50%,#2e6fc4)"></div>
        <h3>Varsity Girls' Tennis...</h3>
        <div class="meta date"><svg width="12" height="12" viewBox="0 0 12 12"><circle cx="6" cy="6" r="5" fill="none" stroke="#888"/><path d="M6 3v3h2" stroke="#888" fill="none"/></svg>Fri, March 28</div>
        <div class="meta place"><svg width="8" height="11" viewBox="0 0 8 11"><path d="M4 0a4 4 0 0 0-4 4c0 3 4 7 4 7s4-4 4-7a4 4 0 0 0-4-4z" fill="#bbb"/></svg>East Linden Street, United States</div>
      </article>
      <article class="news-card">
        <div class="news-photo" role="img" aria-label="Soccer ball on a dark field" style="background:linear-gradient(135deg,#2a2a2a,#8a8a8a 50%,#3a3a3a)"></div>
        <h3>Varsity Boys' Home Soccer...</h3>
        <div class="meta date"><svg width="12" height="12" viewBox="0 0 12 12"><circle cx="6" cy="6" r="5" fill="none" stroke="#888"/><path d="M6 3v3h2" stroke="#888" fill="none"/></svg>Wed, April 30</div>
        <div class="meta place"><svg width="8" height="11" viewBox="0 0 8 11"><path d="M4 0a4 4 0 0 0-4 4c0 3 4 7 4 7s4-4 4-7a4 4 0 0 0-4-4z" fill="#bbb"/></svg>East Linden Street, United States</div>
      </article>
    </div>
  </section>

  <section class="events">
    <h2 class="section-label">Current Events</h2>
    <div class="events-grid">
      <article class="event-card">
        <div class="event-photo" role="img" aria-label="Basketball player shooting at a hoop" style="background:linear-gradient(160deg,#f0e6d8,#b58a60 55%,#5a3a25)"></div>
        <div class="meta when"><svg width="11" height="11" viewBox="0 0 11 11"><rect x=".5" y="1.5" width="10" height="9" fill="none" stroke="#bbb"/></svg>Varsity Boys' Soccer&nbsp; (Mon, March 31)</div>
        <div class="meta where"><svg width="8" height="11" viewBox="0 0 8 11"><path d="M4 0a4 4 0 0 0-4 4c0 3 4 7 4 7s4-4 4-7a4 4 0 0 0-4-4z" fill="#bbb"/></svg>East Linden Street, United States</div>
        <p>Lorem ipsum dolor sit amet, consectetur adipisicing elit, sed do eiusmod tempor incididunt ut labore et dolore magna aliqua. Ut</p>
        <span class="btn-ghost">Read More</span>
      </article>
      <article class="event-card">
        <div class="event-photo" role="img" aria-label="Dancers performing on a dark stage" style="background:linear-gradient(180deg,#0d1630,#1e3870 60%,#2a4a8a)"></div>
        <div class="meta when"><svg width="11" height="11" viewBox="0 0 11 11"><rect x=".5" y="1.5" width="10" height="9" fill="none" stroke="#bbb"/></svg>Varsity Boys' Soccer&nbsp; (Mon, March 31)</div>
        <div class="meta where"><svg width="8" height="11" viewBox="0 0 8 11"><path d="M4 0a4 4 0 0 0-4 4c0 3 4 7 4 7s4-4 4-7a4 4 0 0 0-4-4z" fill="#bbb"/></svg>East Linden Street, United States</div>
        <p>Lorem ipsum dolor sit amet, consectetur adipisicing elit, sed do eiusmod tempor incididunt ut labore et dolore magna aliqua. Ut</p>
        <span class="btn-ghost">Read More</span>
      </article>
      <article class="event-card">
        <div class="event-photo" role="img" aria-label="Student playing a piano" style="background:linear-gradient(120deg,#3a302a,#c7bfb2 60%,#e8e4dc)"></div>
        <div class="meta when"><svg width="11" height="11" viewBox="0 0 11 11"><rect x=".5" y="1.5" width="10" height="9" fill="none" stroke="#bbb"/></svg>Varsity Boys' Soccer&nbsp; (Mon, March 31)</div>
        <div class="meta where"><svg width="8" height="11" viewBox="0 0 8 11"><path d="M4 0a4 4 0 0 0-4 4c0 3 4 7 4 7s4-4 4-7a4 4 0 0 0-4-4z" fill="#bbb"/></svg>East Linden Street, United States</div>
        <p>Lorem ipsum dolor sit amet, consectetur adipisicing elit, sed do eiusmod tempor incididunt ut labore et dolore magna aliqua. Ut</p>
        <span class="btn-ghost">Read More</span>
      </article>
    </div>
  </section>

  <section class="upcoming">
    <h2 class="section-label">UPCOMING EVENTS</h2>
    <div class="upcoming-grid">
      <article class="upcoming-item">
        <div class="ring"><div role="img" aria-label="Students working together at a table" style="background:radial-gradient(circle,#d8d0c4,#4a3c34)"></div></div>
        <h3>Varsity Boys' Soccer match</h3>
        <p>Lorem ipsum dolor sit amet, modi eveniet fugiat quis minus...</p>
      </article>
      <article class="upcoming-item">
        <div class="ring"><div role="img" aria-label="Cheering student at a pep rally" style="background:radial-gradient(circle,#e07a80,#5a1a24)"></div></div>
        <h3>Varsity Boys' Soccer match</h3>
        <p>Lorem ipsum dolor sit amet, modi eveniet fugiat quis minus...</p>
      </article>
      <article class="upcoming-item">
        <div class="ring"><div role="img" aria-label="Theatre cast celebrating on stage" style="background:radial-gradient(circle,#f0c0a0,#c0504a)"></div></div>
        <h3>Varsity Boys' Soccer match</h3>
        <p>Lorem ipsum dolor sit amet, modi eveniet fugiat quis minus...</p>
      </article>
      <article class="upcoming-item">
        <div class="ring"><div role="img" aria-label="Brick school building with lawn" style="background:linear-gradient(180deg,#a7c4e0 0%,#8a5a40 35%,#7a4e36 70%,#6a9a3a 100%)"></div></div>
        <h3>Varsity Boys' Soccer match</h3>
        <p>Lorem ipsum dolor sit amet, modi eveniet fugiat quis minus...</p>
      </article>
    </div>
  </section>

  <footer class="site-footer">
    <div class="footer-col" style="left:22px">
      <h4>CONTACT INFO</h4>
      <div class="contact-line"><svg width="8" height="11" viewBox="0 0 8 11"><path d="M4 0a4 4 0 0 0-4 4c0 3 4 7 4 7s4-4 4-7a4 4 0 0 0-4-4z" fill="#888"/></svg><span>418 East Linden Street<br>Dalton Ridge, VA 23990, United States</span></div>
      <div class="contact-line"><svg width="8" height="12" viewBox="0 0 8 12"><rect width="8" height="12" rx="1.5" fill="#888"/></svg><span>+1 555-014-2236</span></div>
      <div class="contact-line"><svg width="11" height="8" viewBox="0 0 11 8"><rect width="11" height="8" fill="#888"/></svg><span>info@marlowevalley.org</span></div>
    </div>
    <div class="footer-col" style="left:324px">
      <h4>Recent Blog Posts</h4>
      <div class="post">The MVRGS Dance department enjoys an partnership with the Harbor City Ballet.<small>july 7, 2014</small></div>
      <div class="post">The MVRGS Dance department enjoys an partnership with the Harbor City Ballet.<small>july 7, 2014</small></div>
    </div>
    <div class="footer-col" style="left:640px">
      <h4>Subscribe to our Newsletter</h4>
      <div class="mail-field">Enter Your Mail Id</div>
      <div class="btn-sub">Subscribe</div>
    </div>
    <div class="footer-col" style="left:890px">
      <h4>Follow Us</h4>
      <div class="social"><span></span><span></span><span></span></div>
    </div>
  </footer>
  <div class="copyright">© Copyright 2014 Marlowe Valley Regional Governor's School. All Rights Reserved</div>

</div>
</body>
</html>
```